依頼詳細
インターネット通販の本格的な正統派バレエショップ(ヨーロッパ風)を目指していますので、それに合うデザインと同時に、色のレギュレーションなどを決めてプロっぽいホームページを作りたいと思っています。
現在のホームページは色々な色があり、色のレギュレーションが出来ていませんので、今回のリニューアルと同時にメインカラー、ザブカラー、アクセントカラーなどを決めてプロっぽいページ作成をする為に依頼をしました。

既にロゴは決めているので、添付したロゴの色とイメージに合わせて作って下さい。

サイトURL
www.kolvimeta.com
ページ数
1ページ
希望イメージ
シンプル 複雑
単色 カラフル
暗い 明るい
日常 高級
遊び心 厳粛
未来的 伝統的
女性的 男性的
希望する色
紫系、白のベースカラーにロゴ色である藤色をサブカラーと考えています。
納品ファイル
• イラストレーター形式 (.ai)
• フォトショップ形式 (.psd)
補足説明
ロゴを添付しました。
上部分の看板についてですが、添付しました看板を参考にお願いします。
現在のページですと看板が高く下にスクロールをしないと情報が見れないので、
直にわかるように看板を縦に短くしたいです。

報告が遅くなり大変申し訳ございませんでした。
■ 選んだ理由

ターゲットの年齢層にマッチしたデザインと、色使いがとても気に入りました。

■ 提案者全員のお礼・コメント

沢山の方がデザインをして下さり大変嬉しく思います。本当にありがとうございました。

```html
<!DOCTYPE html>
<html lang="ja">
<head>
<meta charset="utf-8">
<title>Kolvimeta バレエ用品専門店</title>
<link href="https://fonts.googleapis.com/css2?family=Noto+Sans+JP:wght@400;700&family=Noto+Serif+JP:wght@400;700&display=swap" rel="stylesheet">
<style>
:root{
  --purple:#5a3d8c;
  --purple-dark:#3f2a66;
  --wisteria:#b7a3d8;
  --lavender:#e9e2f3;
  --lavender-pale:#f5f1fa;
  --page-bg:#e6e3ea;
  --line:#d4cbe3;
  --text:#333;
  --muted:#777;
  --pink:#f6dfe4;
  --pink-deep:#e06a8a;
  --red:#d23a3a;
  --peach:#fbeee2;
  --white:#fff;
}
*{box-sizing:border-box;margin:0;padding:0}
html,body{width:1200px;height:4000px;overflow:hidden}
body{background:var(--page-bg);font-family:"Noto Sans JP",sans-serif;color:var(--text);font-size:13px;line-height:1.5}
.page{position:relative;width:1200px;height:4000px;background:var(--white)}
.topline{height:18px;background:var(--lavender);font-size:10px;color:var(--muted);padding:2px 40px}
.header{height:86px;display:flex;align-items:center;justify-content:space-between;padding:0 40px}
.logo{display:flex;align-items:center;gap:10px;font-size:34px;color:var(--purple);font-weight:700}
.logo-dot{width:16px;height:16px;border-radius:50%;background:var(--wisteria)}
.logo small{display:block;font-size:11px;font-weight:400;color:var(--muted)}
.header-right{text-align:right}
.header-links{font-size:11px;color:var(--muted);margin-bottom:6px}
.header-tel{display:inline-flex;align-items:center;gap:8px;border:2px solid var(--wisteria);padding:4px 14px;border-radius:4px}
.header-tel b{font-size:28px;color:var(--purple);letter-spacing:1px}
.header-tel span{font-size:10px;color:var(--muted);text-align:left}
.gnav{margin:0 40px;height:34px;display:flex;background:var(--lavender-pale);border:1px solid var(--line)}
.gnav li{list-style:none;flex:1;text-align:center;font-size:12px;line-height:32px;border-right:1px solid var(--line);color:var(--purple)}
.gnav li:last-child{border-right:0}
.hero{margin:10px 40px 0;height:282px;background:linear-gradient(180deg,#d9cfc4 0%,#c9b8a6 55%,#b89a82 100%)}
.cols{position:absolute;top:430px;left:40px;width:1120px;display:flex;gap:14px}
.side{width:230px}
.main{width:876px}
.box{border:1px solid var(--line);margin-bottom:14px}
.box-title{background:var(--purple);color:var(--white);font-size:12px;padding:4px 10px;font-weight:700}
.tel-box{padding:10px;background:var(--lavender-pale)}
.tel-box .num{font-size:26px;font-weight:700;color:var(--purple)}
.tel-box .fax{font-size:20px;font-weight:700;color:var(--purple-dark)}
.tel-box p{font-size:10px;color:var(--muted)}
.btn{display:block;background:var(--pink-deep);color:var(--white);text-align:center;font-size:11px;padding:4px;margin-top:6px;border-radius:3px}
.search{display:flex;padding:8px;gap:4px}
.search .field{flex:1;height:24px;border:1px solid var(--line)}
.search .go{width:60px;height:24px;background:var(--purple);color:var(--white);font-size:11px;text-align:center;line-height:24px}
.list li{list-style:none;font-size:11px;padding:4px 10px;border-bottom:1px dotted var(--line)}
.colors{display:grid;grid-template-columns:repeat(4,1fr);gap:10px;padding:12px 18px}
.colors i{display:block;width:28px;height:28px;border-radius:50%;margin:auto}
.banner{height:54px;margin:8px;border:1px solid var(--line);display:flex;align-items:center;justify-content:center;font-size:13px;font-weight:700;color:var(--purple);background:var(--lavender-pale)}
.cat li{list-style:none;display:flex;align-items:center;gap:10px;padding:10px;border-bottom:1px solid var(--line);font-size:12px;height:64px}
.thumb{width:44px;height:44px;background:linear-gradient(135deg,#efe6f5,#d8c8e6);flex:none}
.cal{width:100%;border-collapse:collapse;font-size:11px;text-align:center}
.cal td,.cal th{border:1px solid var(--line);height:28px}
.cal .off{background:var(--pink);color:var(--red)}
.cal-note{font-size:11px;padding:8px}
.notice{padding:10px;font-size:11px;border:2px solid var(--pink-deep);background:var(--peach)}
.notice b{color:var(--red)}
.topics{margin-bottom:14px;border:1px solid var(--line)}
.topics li{list-style:none;font-size:11px;padding:6px 10px;border-bottom:1px dotted var(--line)}
.topics li em{font-style:normal;background:var(--pink-deep);color:#fff;font-size:9px;padding:0 4px;margin-right:6px}
.sec-title{background:linear-gradient(90deg,var(--purple),var(--wisteria));color:#fff;font-size:14px;font-weight:700;padding:6px 12px}
.grid{display:grid;grid-template-columns:repeat(6,1fr);gap:12px;padding:12px;border:1px solid var(--line);margin-bottom:14px}
.item .ph{height:130px;background:linear-gradient(160deg,#f3eef7,#cdbfe0)}
.item p{font-size:10px;margin-top:4px;height:30px;overflow:hidden}
.item b{font-size:11px;color:var(--red)}
.tabs{display:flex;gap:4px;padding:8px 12px 0}
.tabs span{flex:1;background:var(--lavender);font-size:11px;text-align:center;padding:4px;color:var(--purple)}
.tabs span.on{background:var(--purple);color:#fff}
.voice{background:var(--peach);border:1px solid #ead4c0;padding:12px;margin-bottom:14px}
.voice-head{background:var(--purple);color:#fff;font-family:"Noto Serif JP",serif;font-size:18px;padding:6px 14px;border-radius:16px;display:inline-block;margin-bottom:10px}
.voice-grid{display:grid;grid-template-columns:1fr 1fr;gap:10px}
.bubble{background:#fff;border-radius:8px;padding:8px 10px;font-size:11px;height:64px}
.bubble b{color:var(--purple)}
.two{display:flex;gap:14px;margin-bottom:14px}
.two .box{flex:1;margin:0;height:500px}
.post{display:flex;gap:8px;padding:8px;border-bottom:1px dotted var(--line);font-size:11px}
.post .thumb{width:54px;height:54px}
.intro{height:110px;background:linear-gradient(90deg,var(--lavender),#fff);border:1px solid var(--line);display:flex;align-items:center;justify-content:space-between;padding:0 20px;margin-bottom:14px}
.intro h2{font-family:"Noto Serif JP",serif;font-size:22px;color:var(--purple)}
.intro ul li{list-style:none;font-size:12px;color:var(--purple-dark)}
.intro-ph{width:110px;height:90px;background:linear-gradient(180deg,#f1ebf6,#cbb9dd)}
.merit{background:var(--pink);padding:14px;margin-bottom:0}
.merit-lead{text-align:center;font-size:13px;color:var(--pink-deep);font-weight:700;margin-bottom:10px}
.merit-row{display:flex;gap:16px;justify-content:center}
.merit-row div{width:120px;height:120px;border-radius:50%;background:#fff;display:flex;align-items:center;justify-content:center;text-align:center;font-size:12px;color:var(--pink-deep);font-weight:700;border:2px dashed var(--pink-deep)}
.merit-row p{width:260px;font-size:11px;align-self:center}
.ship{background:var(--red);color:#fff;font-size:18px;font-weight:700;text-align:center;padding:8px}
.footer{position:absolute;top:2600px;left:40px;width:1120px;display:flex;gap:14px}
.footer .box{flex:1;height:1320px}
.footer p{font-size:11px;padding:4px 12px}
.bottom{position:absolute;bottom:0;left:0;width:1200px;height:40px;background:var(--purple);color:#fff;font-size:11px;text-align:center;line-height:40px}
</style>
</head>
<body>
<div class="page">
  <div class="topline">バレエ用品の通販ならコルヴィメタ。本格派のレオタード・シューズをお届けします。</div>
  <header class="header">
    <div class="logo"><span class="logo-dot"></span><div>Kolvimeta<small>バレエ用品専門店</small></div></div>
    <div class="header-right">
      <div class="header-links">トップページ ｜ 初めての方 ｜ 会社概要 ｜ 送料・支払 ｜ お問い合わせ ｜ カートを見る</div>
      <div class="header-tel"><span>お電話でのご注文<br>平日 10:00〜18:00</span><b>0120-415-276</b></div>
    </div>
  </header>
  <ul class="gnav">
    <li>レオタード</li><li>バレエシューズ</li><li>タイツ</li><li>スカート</li><li>ウォームアップ</li><li>バッグ</li><li>小物</li><li>セール</li>
  </ul>
  <div class="hero" role="img" aria-label="バーレッスンをする少女たちの写真"></div>

  <div class="cols">
    <aside class="side">
      <div class="box tel-box">
        <p>バレエ講師のスタッフが対応します</p>
        <div class="num">0120-415-276</div>
        <p>平日 10:00〜18:00</p>
        <div class="fax">FAX：03-5820-1147</div>
        <span class="btn">メールでのお問い合わせ</span>
      </div>
      <div class="box"><div class="box-title">商品検索</div><div class="search"><span class="field"></span><span class="go">Search</span></div></div>
      <div class="box"><div class="box-title">PICK UP KEYWORD</div>
        <ul class="list"><li>レオタード 子供</li><li>バレエシューズ 布</li><li>巻きスカート</li><li>タイツ 穴あき</li><li>ウォームアップ</li></ul></div>
      <div class="box"><div class="box-title">COLOR SELECT</div>
        <div class="colors">
          <i style="background:#111"></i><i style="background:#fff;border:1px solid #ccc"></i><i style="background:#f2b8c6"></i><i style="background:#c63a4a"></i>
          <i style="background:#9b7fc8"></i><i style="background:#5a3d8c"></i><i style="background:#3a6fb0"></i><i style="background:#8fc6e8"></i>
          <i style="background:#6ab27a"></i><i style="background:#f4d36a"></i><i style="background:#f29a4a"></i><i style="background:#9a7a5a"></i>
        </div></div>
      <div class="box"><div class="box-title">PICK UP</div>
        <div class="banner">コーディネート特集</div><div class="banner">お得な福袋</div><div class="banner">会員限定メルマガ</div></div>
      <div class="box"><div class="box-title">ITEM CATEGORY</div>
        <ul class="cat">
          <li><span class="thumb" role="img" aria-label="入門セット"></span>入門セット</li>
          <li><span class="thumb" role="img" aria-label="子供用レオタード"></span>子供用レオタード</li>
          <li><span class="thumb" role="img" aria-label="大人用レオタード"></span>大人用レオタード</li>
          <li><span class="thumb" role="img" aria-label="ジュニアレオタード"></span>ジュニア・大人用</li>
          <li><span class="thumb" role="img" aria-label="バレエシューズ"></span>バレエシューズ</li>
          <li><span class="thumb" role="img" aria-label="タイツ"></span>タイツ</li>
          <li><span class="thumb" role="img" aria-label="アンダーウェア"></span>アンダーウェア</li>
          <li><span class="thumb" role="img" aria-label="スカート"></span>スカート</li>
          <li><span class="thumb" role="img" aria-label="ウォームアップ"></span>ウォームアップ</li>
          <li><span class="thumb" role="img" aria-label="ウォームアップ小物"></span>ウォームアップ小物</li>
          <li><span class="thumb" role="img" aria-label="レッスンバッグ"></span>レッスンバッグ</li>
          <li><span class="thumb" role="img" aria-label="バレエ雑貨"></span>バレエ雑貨</li>
        </ul></div>
      <div class="box"><div class="box-title">2014年8月</div>
        <table class="cal">
          <tr><th>日</th><th>月</th><th>火</th><th>水</th><th>木</th><th>金</th><th>土</th></tr>
          <tr><td></td><td></td><td></td><td></td><td></td><td>1</td><td class="off">2</td></tr>
          <tr><td class="off">3</td><td>4</td><td>5</td><td>6</td><td>7</td><td>8</td><td class="off">9</td></tr>
          <tr><td class="off">10</td><td>11</td><td>12</td><td>13</td><td>14</td><td>15</td><td class="off">16</td></tr>
          <tr><td class="off">17</td><td>18</td><td>19</td><td>20</td><td>21</td><td>22</td><td class="off">23</td></tr>
          <tr><td class="off">24</td><td>25</td><td>26</td><td>27</td><td>28</td><td>29</td><td class="off">30</td></tr>
          <tr><td class="off">31</td><td></td><td></td><td></td><td></td><td></td><td></td></tr>
        </table>
        <p class="cal-note">赤字は定休日です<br>営業時間：平日 10:00〜18:00<br>土曜 10:00〜15:00</p></div>
      <div class="notice"><b>■ 夏季休業のお知らせ</b><br>誠に勝手ながら下記の期間を休業とさせていただきます。期間中のご注文は休業明けより順次発送いたします。<br><br><b>■ ご注文について</b><br>ご注文はインターネットにて24時間受け付けております。お電話でのご注文は営業時間内にお願いいたします。ご不明な点はお気軽にお問い合わせください。</div>
    </aside>

    <main class="main">
      <div class="topics"><div class="sec-title">Topics</div>
        <ul>
          <li><em>NEW</em>2014.08.01 新作レオタードを入荷しました。人気のカラーもご用意しております。</li>
          <li><em>NEW</em>2014.07.25 夏季休業期間についてのお知らせを掲載しました。</li>
          <li><em>INFO</em>2014.07.18 バレエシューズのサイズ表を更新しました。</li>
          <li><em>INFO</em>2014.07.10 発表会向けのスカート特集を公開しました。</li>
        </ul></div>

      <div class="sec-title">New ITEM 新着アイテム</div>
      <div class="grid">
        <div class="item"><div class="ph" role="img" aria-label="黒のレオタード"></div><p>キャミソールレオタード ブラック</p><b>¥4,320</b></div>
        <div class="item"><div class="ph" role="img" aria-label="ピンクのタイツ"></div><p>フーター付きタイツ ピンク</p><b>¥1,620</b></div>
        <div class="item"><div class="ph" role="img" aria-label="紫のレオタード"></div><p>フレンチ袖レオタード パープル</p><b>¥5,400</b></div>
        <div class="item"><div class="ph" role="img" aria-label="巻きスカート"></div><p>シフォン巻きスカート</p><b>¥2,700</b></div>
        <div class="item"><div class="ph" role="img" aria-label="バレエシューズ"></div><p>布製バレエシューズ</p><b>¥2,160</b></div>
        <div class="item"><div class="ph" role="img" aria-label="ウォームアップ"></div><p>ニットウォームアップ</p><b>¥3,780</b></div>
        <div class="item"><div class="ph" role="img" aria-label="子供用レオタード"></div><p>子供用スカート付きレオタード</p><b>¥3,240</b></div>
        <div class="item"><div class="ph" role="img" aria-label="白のレオタード"></div><p>ホルターネックレオタード</p><b>¥4,860</b></div>
        <div class="item"><div class="ph" role="img" aria-label="ショート丈カーディガン"></div><p>ショート丈カーディガン</p><b>¥3,240</b></div>
        <div class="item"><div class="ph" role="img" aria-label="レッスンバッグ"></div><p>キルティングレッスンバッグ</p><b>¥2,980</b></div>
        <div class="item"><div class="ph" role="img" aria-label="ヘアアクセサリー"></div><p>シニヨンネットセット</p><b>¥864</b></div>
        <div class="item"><div class="ph" role="img" aria-label="ベロアレオタード"></div><p>ベロア長袖レオタード</p><b>¥6,480</b></div>
      </div>

      <div class="box"><div class="sec-title">ITEM RANKING 売れ筋ランキング</div>
        <div class="tabs"><span class="on">レオタード</span><span>シューズ</span><span>タイツ</span><span>スカート</span><span>ウォームアップ</span><span>小物</span></div>
        <div class="grid" style="border:0;margin:0">
          <div class="item"><div class="ph" role="img" aria-label="1位の商品"></div><p>1位 定番キャミレオタード</p><b>¥3,980</b></div>
          <div class="item"><div class="ph" role="img" aria-label="2位の商品"></div><p>2位 子供用半袖レオタード</p><b>¥3,240</b></div>
          <div class="item"><div class="ph" role="img" aria-label="3位の商品"></div><p>3位 スカート付きレオタード</p><b>¥4,320</b></div>
          <div class="item"><div class="ph" role="img" aria-label="4位の商品"></div><p>4位 フレンチ袖レオタード</p><b>¥5,400</b></div>
          <div class="item"><div class="ph" role="img" aria-label="5位の商品"></div><p>5位 タンクレオタード</p><b>¥3,780</b></div>
          <div class="item"><div class="ph" role="img" aria-label="6位の商品"></div><p>6位 ベロアレオタード</p><b>¥6,480</b></div>
        </div></div>

      <div class="voice">
        <div class="voice-head">Customer's Voice</div>
        <div class="voice-grid">
          <div class="bubble"><b>東京都 M様</b><br>サイズの相談に丁寧に乗っていただき、娘にぴったりのレオタードが見つかりました。</div>
          <div class="bubble"><b>大阪府 K様</b><br>注文の翌日に届いて発表会に間に合いました。梱包もとても綺麗でした。</div>
          <div class="bubble"><b>愛知県 S様</b><br>色の種類が多く、教室の指定色もすぐに揃えることができて助かりました。</div>
          <div class="bubble"><b>福岡県 T様</b><br>生地がしっかりしていて洗濯しても型崩れしません。また利用します。</div>
        </div></div>

      <div class="two">
        <div class="box"><div class="box-title">ブログ</div>
          <div class="post"><span class="thumb" role="img" aria-label="ブログ写真"></span><div><b>スタッフ日記</b><br>新作のレオタードが入荷しました。</div></div>
          <div class="post"><span class="thumb" role="img" aria-label="ブログ写真"></span><div><b>レッスンのこと</b><br>バーレッスン前の準備について。</div></div>
          <div class="post"><span class="thumb" role="img" aria-label="ブログ写真"></span><div><b>スタッフ日記</b><br>発表会シーズンのおすすめ小物。</div></div>
          <div class="post"><span class="thumb" role="img" aria-label="ブログ写真"></span><div><b>お知らせ</b><br>夏季休業期間のご案内です。</div></div>
          <div class="post"><span class="thumb" role="img" aria-label="ブログ写真"></span><div><b>商品紹介</b><br>シューズの選び方をご紹介します。</div></div>
          <div class="post"><span class="thumb" role="img" aria-label="ブログ写真"></span><div><b>スタッフ日記</b><br>教室見学に伺いました。</div></div>
        </div>
        <div class="box"><div class="box-title">Timeline</div>
          <div class="post"><span class="thumb"></span><div><b>Kolvimeta</b><br>本日入荷の新作をご紹介します。</div></div>
          <div class="post"><span class="thumb"></span><div><b>Kolvimeta</b><br>サイズ交換は無料で承ります。</div></div>
          <div class="post"><span class="thumb"></span><div><b>Kolvimeta</b><br>週末セールを開催中です。</div></div>
          <div class="post"><span class="thumb"></span><div><b>Kolvimeta</b><br>人気のタイツが再入荷しました。</div></div>
          <div class="post"><span class="thumb"></span><div><b>Kolvimeta</b><br>明日は定休日となります。</div></div>
          <div class="post"><span class="thumb"></span><div><b>Kolvimeta</b><br>メルマガ会員を募集中です。</div></div>
        </div>
      </div>

      <div class="intro">
        <div><h2>先生も お勧め！「コルヴィメタ」のご紹介</h2>
          <ul><li>◆ 正統派バレエ用品のみを厳選</li><li>◆ メーカー正規品を豊富に在庫</li><li>◆ バレエ専門スタッフが対応</li></ul></div>
        <div class="intro-ph" role="img" aria-label="バレエを踊る女性の写真"></div>
      </div>

      <div class="merit">
        <p class="merit-lead">当店では有名バレエ教室の先生にも選ばれる安心のサービスをご用意しております</p>
        <div class="merit-row">
          <div>安心の<br>サイズ交換</div><div>豊富な<br>品揃え</div><div>即日発送<br>対応</div>
          <p>インターネットでのお買い物が初めての方も安心してご利用いただけるよう、サイズ選びから発送まで専門スタッフが丁寧にサポートいたします。</p>
        </div>
      </div>
      <div class="ship">送料 全国一律200円　3000円以上のご注文で無料</div>
    </main>
  </div>

  <div class="footer">
    <div class="box"><div class="box-title">お店について</div>
      <p>ショップ名：Kolvimeta バレエ用品専門店</p><p>運営：株式会社コルヴィメタ</p><p>TEL：0120-415-276</p><p>FAX：03-5820-1147</p><p>営業時間：平日 10:00〜18:00</p><p>定休日：日曜・祝日</p><p>URL：www.kolvimeta.com</p></div>
    <div class="box"><div class="box-title">ご利用案内</div>
      <p>■ お支払い方法<br>クレジットカード、代金引換、銀行振込がご利用いただけます。</p><p>■ 送料<br>全国一律200円、3000円以上で無料です。</p><p>■ 返品・交換<br>商品到着後7日以内にご連絡ください。</p></div>
    <div class="box"><div class="box-title">お届けについて</div>
      <p>■ 発送について<br>15時までのご注文は当日発送いたします。</p><p>■ 配送業者<br>提携の宅配便にてお届けします。</p><p>■ お届け日時<br>ご希望の日時を指定いただけます。</p></div>
  </div>
  <div class="bottom">Copyright © Kolvimeta All Rights Reserved.</div>
</div>
</body>
</html>
```